Computer repair services flyer

This flyer / leaflet is required to promote my local computer and laptop repair business. It will primarily be used for pinning to notice boards when I get access to shared accommodation but I will also use it in the future for posting through letterboxes in affluent areas.

Company branding, logo, services, pricing, contact details etc. can be found on my website at : www.brightmendlaptops.co.uk

The services I would predominantly like to promote on this flyer are :

Speeding up slow / old computers
Virus removal
Lost data recovered
Broken laptop screen replacements
Dead laptops fixed
We buy and recycle broken laptops for cash

Other features to highlight :

Friendly and experienced
We are local (Near to Cardiff city center)
Quick repair turnaround - most repairs within 24hours
Affordable / No VAT
Free diagnostics
No Fix = No fee
Free collection and delivery
We Guarantee our work

Calls to action and attention grabbing if possible. Offer 10% off. Free cooling fan clean.

Size of flyer = A5 (210 x 148mm or 8.3 x 5.8in) portrait, single sided colour.

Target Market(s)

18 to 60 years

Industry/Entity Type

Accommodation

Requirements
Must have
• 02920 413657

```html
<!DOCTYPE html>
<html lang="en">
<head>
<meta charset="utf-8">
<title>BrightMend Laptops – Computer Repair Flyer</title>
<link href="https://fonts.googleapis.com/css2?family=Open+Sans:wght@400;600;700&display=swap" rel="stylesheet">
<style>
:root{
  --orange:#f08a24;
  --orange-light:#f7a654;
  --orange-dark:#d9731a;
  --ink:#1f1f1f;
  --tile-dark:#262626;
  --tile-mid:#3a3a3a;
  --text:#222;
  --muted:#8a8a8a;
  --footer-text:#6d6d6d;
  --white:#fff;
}
*{margin:0;padding:0;box-sizing:border-box}
html,body{width:846px;height:1200px;overflow:hidden;background:var(--white)}
body{font-family:"Open Sans",Arial,sans-serif;color:var(--text)}
.flyer{position:relative;width:846px;height:1200px;overflow:hidden;background:var(--white)}
.block{position:absolute}
.dark{background:linear-gradient(90deg,var(--tile-dark),var(--tile-mid) 60%,var(--tile-dark))}
.orange{background:linear-gradient(90deg,var(--orange-dark),var(--orange-light) 50%,var(--orange-dark))}
.rule-h{position:absolute;height:4px;background:var(--orange)}
.rule-v{position:absolute;width:4px;background:var(--orange)}
.tile{position:absolute;display:flex;align-items:center;justify-content:center;text-align:center;color:var(--white);font-weight:700;line-height:1.3}
.photo{position:absolute}
.photo-cable{background:linear-gradient(135deg,#f4f4f4,#bfc3c8 60%,#6d7f9a)}
.photo-usb{background:linear-gradient(135deg,#ffffff,#d9d9d9 55%,#a48a4a)}
.photo-drive{background:linear-gradient(160deg,#f2f2f2,#cfcfcf 50%,#3a3a3a)}
.photo-gauge{background:radial-gradient(circle at 55% 50%,#4a4a20 0,#1a1a1a 45%,#050505 100%)}
.photo-laptop{background:linear-gradient(135deg,#dfe6ee,#9aa7b6 55%,#3c4450)}
.brand-box{position:absolute;left:50px;top:30px;width:462px;height:205px;background:var(--white);border-radius:14px;box-shadow:0 0 0 3px #e6e6e6;display:flex;align-items:center;justify-content:center;gap:14px}
.brand-dot{width:28px;height:28px;border-radius:50%;background:var(--orange);flex:none}
.brand-name{font-size:37px;font-weight:700;color:var(--ink);letter-spacing:-1px;white-space:nowrap}
.features{position:absolute;left:38px;top:672px;list-style:none}
.features li{display:flex;align-items:center;height:45px;font-size:24.5px}
.features svg{width:36px;height:34px;margin-right:18px;flex:none}
.offer-shadow{position:absolute;left:450px;top:900px;width:385px;height:140px;border-radius:50%;background:radial-gradient(ellipse,#dcdcdc,#f5f5f5 70%,transparent 72%)}
.offer{position:absolute;left:462px;top:828px;width:350px;height:170px;background:var(--ink);border-radius:10px;transform:rotate(-11deg);padding:22px 16px 0 14px;color:var(--orange);font-weight:700;font-size:18.5px;line-height:1.45}
.contact{position:absolute;top:1068px;display:flex;align-items:flex-start}
.divider{position:absolute;top:1068px;width:4px;height:112px;background:var(--orange)}
.address{left:40px;font-size:17px;line-height:25px;color:var(--muted)}
.address svg{margin-right:16px}
.phone-line{position:absolute;left:300px;top:1143px;font-size:25px;font-weight:700;color:var(--footer-text)}
.web-line{position:absolute;right:34px;top:1146px;font-size:21.5px;font-weight:700;color:var(--footer-text);white-space:nowrap}
</style>
</head>
<body>
<main class="flyer">

  <div class="block dark" style="left:0;top:0;width:250px;height:182px"></div>
  <div class="block orange" style="left:258px;top:0;width:194px;height:182px"></div>
  <div class="block dark" style="left:460px;top:0;width:190px;height:182px"></div>

  <div class="photo photo-cable" role="img" aria-label="Network cable plugged into a laptop port" style="left:478px;top:0;width:168px;height:176px"></div>
  <div class="photo photo-usb" role="img" aria-label="USB memory stick close-up" style="left:660px;top:0;width:186px;height:176px"></div>

  <div class="rule-h" style="left:0;top:182px;width:846px"></div>
  <div class="rule-h" style="left:0;top:364px;width:846px"></div>
  <div class="rule-v" style="left:252px;top:0;height:600px"></div>
  <div class="rule-v" style="left:454px;top:0;height:550px"></div>
  <div class="rule-v" style="left:652px;top:0;height:550px"></div>

  <div class="tile dark" style="left:62px;top:240px;width:186px;height:120px;font-size:22px">Speeding up<br>slow / old<br>computers</div>
  <div class="tile orange" style="left:258px;top:240px;width:192px;height:120px;font-size:30px">Virus<br>removal</div>
  <div class="tile dark" style="left:460px;top:240px;width:188px;height:120px;font-size:25px">Lost data<br>recovered</div>
  <div class="photo photo-drive" role="img" aria-label="Laptop with open optical disc drive" style="left:660px;top:190px;width:186px;height:170px"></div>

  <div class="photo photo-gauge" role="img" aria-label="Glowing speedometer dial" style="left:50px;top:372px;width:198px;height:176px"></div>
  <div class="tile dark" style="left:258px;top:372px;width:192px;height:176px;font-size:22px">Broken<br>laptop<br>screen<br>replacements</div>
  <div class="tile orange" style="left:460px;top:372px;width:188px;height:176px;font-size:32px;line-height:1.4">Dead<br>laptops<br>fixed</div>
  <div class="photo photo-laptop" role="img" aria-label="Person relaxing while typing on a laptop" style="left:660px;top:372px;width:186px;height:176px"></div>

  <div class="tile dark" style="left:455px;top:557px;width:391px;height:102px;font-size:26px;line-height:1.35">We buy and recycle<br>broken laptops for cash</div>
  <div class="rule-h" style="left:508px;top:660px;width:338px"></div>

  <div class="brand-box">
    <span class="brand-dot"></span>
    <span class="brand-name">BrightMend Laptops</span>
  </div>

  <ul class="features">
    <li><svg viewBox="0 0 36 34"><ellipse cx="17" cy="14" rx="16" ry="12" fill="#f08a24"/><path d="M10 23 L8 32 L18 25Z" fill="#f08a24"/><text x="17" y="17" font-size="8" font-weight="700" fill="#fff" text-anchor="middle" font-family="Open Sans,sans-serif">YES!</text></svg>Friendly and experienced</li>
    <li><svg viewBox="0 0 36 34"><ellipse cx="17" cy="14" rx="16" ry="12" fill="#f08a24"/><path d="M10 23 L8 32 L18 25Z" fill="#f08a24"/><text x="17" y="17" font-size="8" font-weight="700" fill="#fff" text-anchor="middle" font-family="Open Sans,sans-serif">YES!</text></svg>We are local (Near to Cardiff city center)</li>
    <li><svg viewBox="0 0 36 34"><ellipse cx="17" cy="14" rx="16" ry="12" fill="#f08a24"/><path d="M10 23 L8 32 L18 25Z" fill="#f08a24"/><text x="17" y="17" font-size="8" font-weight="700" fill="#fff" text-anchor="middle" font-family="Open Sans,sans-serif">YES!</text></svg>Quick repair turnaround - most repairs within 24hours</li>
    <li><svg viewBox="0 0 36 34"><ellipse cx="17" cy="14" rx="16" ry="12" fill="#f08a24"/><path d="M10 23 L8 32 L18 25Z" fill="#f08a24"/><text x="17" y="17" font-size="8" font-weight="700" fill="#fff" text-anchor="middle" font-family="Open Sans,sans-serif">YES!</text></svg>Affordable / No VAT</li>
    <li><svg viewBox="0 0 36 34"><ellipse cx="17" cy="14" rx="16" ry="12" fill="#f08a24"/><path d="M10 23 L8 32 L18 25Z" fill="#f08a24"/><text x="17" y="17" font-size="8" font-weight="700" fill="#fff" text-anchor="middle" font-family="Open Sans,sans-serif">YES!</text></svg>Free diagnostics</li>
    <li><svg viewBox="0 0 36 34"><ellipse cx="17" cy="14" rx="16" ry="12" fill="#f08a24"/><path d="M10 23 L8 32 L18 25Z" fill="#f08a24"/><text x="17" y="17" font-size="8" font-weight="700" fill="#fff" text-anchor="middle" font-family="Open Sans,sans-serif">YES!</text></svg>No Fix = No fee</li>
    <li><svg viewBox="0 0 36 34"><ellipse cx="17" cy="14" rx="16" ry="12" fill="#f08a24"/><path d="M10 23 L8 32 L18 25Z" fill="#f08a24"/><text x="17" y="17" font-size="8" font-weight="700" fill="#fff" text-anchor="middle" font-family="Open Sans,sans-serif">YES!</text></svg>Free collection and delivery</li>
    <li><svg viewBox="0 0 36 34"><ellipse cx="17" cy="14" rx="16" ry="12" fill="#f08a24"/><path d="M10 23 L8 32 L18 25Z" fill="#f08a24"/><text x="17" y="17" font-size="8" font-weight="700" fill="#fff" text-anchor="middle" font-family="Open Sans,sans-serif">YES!</text></svg>We Guarantee our work</li>
  </ul>

  <div class="offer-shadow"></div>
  <div class="offer">Calls to action and attention<br>grabbing if possible.<br>Offer 10% off.<br>Free cooling fan clean</div>

  <div class="contact address">
    <svg width="54" height="90" viewBox="0 0 54 90"><circle cx="27" cy="8" r="6" fill="none" stroke="#f08a24" stroke-width="4"/><circle cx="27" cy="46" r="26" fill="#f08a24"/><circle cx="27" cy="46" r="18" fill="#fff"/><path d="M27 32 L31 46 L27 60 L23 46Z" fill="#f08a24"/></svg>
    <div>14 Alder Grove<br>Llanishen<br>Cardiff<br>CF14 2QT</div>
  </div>
  <div class="divider" style="left:268px"></div>

  <svg class="block" style="left:352px;top:1068px" width="56" height="62" viewBox="0 0 56 62"><path d="M6 20 Q28 4 50 20 L46 28 L38 24 L38 18 Q28 14 18 18 L18 24 L10 28Z" fill="#f08a24"/><path d="M12 30 L44 30 L52 58 L4 58Z" fill="#f08a24"/><circle cx="28" cy="43" r="9" fill="#fff"/><circle cx="28" cy="43" r="4" fill="#f08a24"/></svg>
  <div class="phone-line">02920 413657</div>
  <div class="divider" style="left:510px"></div>

  <svg class="block" style="left:628px;top:1068px" width="70" height="64" viewBox="0 0 70 64"><circle cx="32" cy="32" r="28" fill="#d6d6d6"/><ellipse cx="32" cy="32" rx="12" ry="28" fill="none" stroke="#b0b0b0" stroke-width="2"/><line x1="4" y1="32" x2="60" y2="32" stroke="#b0b0b0" stroke-width="2"/><path d="M2 40 Q34 26 68 30" fill="none" stroke="#f08a24" stroke-width="4"/></svg>
  <div class="web-line">brightmendlaptops.co.uk</div>

</main>
</body>
</html>
```